Design a styled business card for an intimacy and attachment psychologist

I am a Psychologist providing online therapy to patients across the United States. My work is interpersonal and emotion-focused, with an emphasis on the client-therapist relationship. My primary areas of work are very personal, including sexuality and gender, abuse and trauma, and grief and loss. My target audience will be adults of all ages 18+.
My business card should convey a warm and inviting feeling of professionalism that is also casual and comfortable.
The front should be fairly simple and professional, consisting of:
- My name, Dr. Rosalind Pembrook
- My title, Licensed Psycholigist
- My logo
On either the front or the back, my contact information should be listed:
- ros@drrospembrook.example
- 555.014.7789
- drrospembrook.example
On the rear, I would like a description of the areas that I specialize in. This can be formatted in any way that appears stylistically interesting.
Individual and Couples
Relationships and Infidelity
Sexual Health & Aging
Gender Identity & Sexual Orientation
Abuse and Trauma
Sexual Compulsivity & Addiction
Sexual Dysfunction
Target Market(s)
My target audience will be adults of all ages 18+.
Industry/Entity Type
Psychology
Contact Information for Business Card
The front should be fairly simple and professional, consisting of: - My name, Dr. Rosalind Pembrook - My title, Licensed Psycholigist - My logo On either the front or the back, my contact information should be listed: - ros@drrospembrook.example - 555.014.7789 - drrospembrook.example On the rear, I would like a description of the areas that I specialize in. This can be formatted in any way that appears stylistically interesting. Individual and Couples Relationships and Infidelity Sexual Health & Aging Gender Identity & Sexual Orientation Abuse and Trauma Sexual Compulsivity & Addiction Sexual Dysfunction

```html
<!DOCTYPE html>
<html lang="en">
<head>
<meta charset="utf-8">
<title>Dr. Rosalind Pembrook – Business Card</title>
<link rel="stylesheet" href="https://fonts.googleapis.com/css2?family=Cinzel:wght@500&family=Poppins:wght@400;600&display=swap">
<style>
  :root{
    --bg:#d9d7dd;
    --plum:#2c2550;
    --white:#ffffff;
    --ink:#2c2550;
    --grey:#6b6a75;
    --mint:#7fcfb5;
    --mint-pale:#c9e9e2;
    --orange:#f5a623;
    --yellow:#fbc748;
    --coral:#f36b5d;
    --red:#e7413c;
    --violet:#9b5fb5;
  }
  *{box-sizing:border-box;margin:0;padding:0}
  html,body{width:1200px;height:913px;overflow:hidden}
  body{background:var(--bg);font-family:"Poppins",sans-serif;position:relative}

  .card{position:absolute;width:560px;height:320px;border-radius:18px;overflow:hidden;box-shadow:0 10px 30px rgba(30,20,50,.25)}

  /* Back of card */
  .card--back{left:50px;top:110px;background:var(--plum);color:var(--white)}
  .card--back .brand-name{position:absolute;left:36px;top:92px;font-family:"Cinzel",serif;font-weight:500;font-size:30px;line-height:1.05;color:var(--white);letter-spacing:1px}
  .specialties{position:absolute;left:36px;top:178px;list-style:none;font-size:12.5px;line-height:18px;color:var(--white)}
  .specialties li{display:flex;align-items:center;gap:9px}
  .specialties li::before{content:"";width:5px;height:5px;border-radius:50%;background:var(--dot)}
  .emblem-area{position:absolute;right:-40px;top:-70px;width:320px;height:320px}

  /* Front of card */
  .card--front{left:590px;top:470px;background:var(--white)}
  .logo{position:absolute;left:34px;top:42px;display:flex;align-items:center;gap:14px}
  .logo-dot{width:56px;height:56px;border-radius:50%;background:var(--mint)}
  .logo-name{font-family:"Cinzel",serif;font-weight:500;font-size:22px;line-height:1.05;color:var(--ink);width:170px}
  .title-block{position:absolute;right:34px;top:62px;text-align:right}
  .title-block .name{font-weight:600;font-size:19px;color:var(--ink)}
  .title-block .role{font-size:12.5px;color:var(--grey);margin-top:2px}
  .spectrum{position:absolute;left:34px;right:34px;top:170px;height:3px;border-radius:2px;
    background:linear-gradient(90deg,var(--ink) 0%,var(--ink) 12%,var(--orange) 25%,var(--yellow) 38%,var(--red) 55%,var(--violet) 75%,var(--mint) 90%,var(--mint-pale) 100%)}
  .contacts{position:absolute;left:34px;top:196px;list-style:none;font-size:14px;line-height:27px;color:var(--ink)}
  .contacts li{display:flex;align-items:center;gap:10px}
  .contacts svg{width:14px;height:14px;flex:none}
</style>
</head>
<body>

<section class="card card--back" aria-label="Back of business card">
  <div class="emblem-area">
    <svg viewBox="0 0 320 320" width="320" height="320" role="img" aria-label="Practice emblem area">
      <circle cx="160" cy="160" r="152" fill="none" stroke="#ffffff" stroke-width="7"/>
      <circle cx="160" cy="160" r="138" fill="#a9dccf"/>
    </svg>
  </div>
  <div class="brand-name">Dr. Rosalind<br>Pembrook</div>
  <ul class="specialties">
    <li style="--dot:var(--orange)">Individual and Couples</li>
    <li style="--dot:var(--yellow)">Relationships and Infidelity</li>
    <li style="--dot:var(--coral)">Sexual Health &amp; Aging</li>
    <li style="--dot:var(--red)">Gender Identity &amp; Sexual Orientation</li>
    <li style="--dot:var(--violet)">Abuse and Trauma</li>
    <li style="--dot:var(--violet)">Sexual Compulsivity &amp; Addiction</li>
    <li style="--dot:var(--mint)">Sexual Dysfunction</li>
  </ul>
</section>

<section class="card card--front" aria-label="Front of business card">
  <div class="logo">
    <span class="logo-dot"></span>
    <span class="logo-name">Dr. Rosalind Pembrook</span>
  </div>
  <div class="title-block">
    <div class="name">Dr. Rosalind Pembrook</div>
    <div class="role">Licensed Psycholigist</div>
  </div>
  <div class="spectrum"></div>
  <ul class="contacts">
    <li>
      <svg viewBox="0 0 16 16" aria-hidden="true"><path d="M4 1.5l2.2 3-1.4 1.6c.8 1.8 2.3 3.3 4.1 4.1l1.6-1.4 3 2.2-1.2 2.5C7 13.8 2.2 9 1.5 2.7z" fill="#f5a623"/></svg>
      555.014.7789
    </li>
    <li>
      <svg viewBox="0 0 16 16" aria-hidden="true"><rect x="1" y="3" width="14" height="10" rx="1.5" fill="#e7413c"/><path d="M1.5 4l6.5 5 6.5-5" fill="none" stroke="#fff" stroke-width="1.3"/></svg>
      ros@drrospembrook.example
    </li>
    <li>
      <svg viewBox="0 0 16 16" aria-hidden="true"><circle cx="8" cy="8" r="7" fill="#9b5fb5"/><path d="M1 8h14M8 1c-3 3.5-3 10.5 0 14M8 1c3 3.5 3 10.5 0 14" fill="none" stroke="#fff" stroke-width="1"/></svg>
      drrospembrook.example
    </li>
  </ul>
</section>

</body>
</html>
```